Hot air balloon tour company needs a brochure redesign

Look for a fresh new brochure design. Using company logo and colours.
Modern, simple and professional look required
Font styles to use
Sans Serif
Colors
0054AA
0677BA
7BADD7
CADEEF
E8F1F8

```html
<!DOCTYPE html>
<html lang="en">
<head>
<meta charset="utf-8">
<title>Skyward Ballooning – Hunter Valley Brochure</title>
<link rel="stylesheet" href="https://fonts.googleapis.com/css2?family=Dancing+Script:wght@500;700&family=Open+Sans:wght@400;600&display=swap">
<style>
  :root {
    --blue-deep: #0054AA;
    --blue-mid: #0677BA;
    --blue-bright: #2399cc;
    --blue-panel: #17709a;
    --blue-soft: #7BADD7;
    --blue-pale: #CADEEF;
    --blue-mist: #E8F1F8;
    --ink-dark: #151515;
    --ink-grey: #4a4a4a;
    --white: #ffffff;
    --heading-blue: #2a9fd6;
  }
  * { margin: 0; padding: 0; box-sizing: border-box; }
  html, body { width: 1200px; height: 849px; overflow: hidden; background: var(--white); }
  .brochure {
    position: relative; width: 1200px; height: 849px; overflow: hidden;
    font-family: "Open Sans", sans-serif; color: var(--white);
  }
  .backdrop { position: absolute; inset: 0; }
  .text { position: absolute; }
  .script { font-family: "Dancing Script", cursive; font-weight: 700; color: var(--heading-blue); }
  .feature-title { font-size: 23px; line-height: 1; margin-bottom: 12px; }
  .feature-body { font-size: 14.5px; line-height: 20px; }
  .panel-right .feature-title { color: var(--white); }

  .cover { left: 0; width: 400px; text-align: center; top: 520px; color: var(--ink-grey); }
  .cover-headline { font-size: 62px; line-height: 1; color: var(--heading-blue); font-weight: 500; }
  .cover-sub { font-size: 21px; line-height: 31px; font-weight: 600; margin-top: 8px; color: #555; }
  .cover-phone { font-size: 42px; font-weight: 600; color: var(--heading-blue); margin-top: 14px; line-height: 1.1; }
  .cover-digits { font-size: 20px; font-weight: 600; margin-top: 8px; color: #555; }
  .cover-web { font-size: 20px; font-weight: 600; margin-top: 12px; color: #555; }

  .feature-mid { left: 423px; width: 360px; }
  .feature-right { left: 828px; width: 345px; }

  .brand-name {
    left: 428px; top: 786px; font-size: 18px; font-weight: 600; color: var(--heading-blue);
    display: flex; align-items: center; gap: 8px;
  }
  .brand-dot { width: 14px; height: 14px; border-radius: 50%; background: var(--heading-blue); }
</style>
</head>
<body>
<div class="brochure">
  <svg class="backdrop" width="1200" height="849" viewBox="0 0 1200 849">
    <defs>
      <linearGradient id="darkPanel" x1="0" y1="0" x2="0" y2="1">
        <stop offset="0" stop-color="#262626"/>
        <stop offset="1" stop-color="#0c0c0c"/>
      </linearGradient>
      <linearGradient id="vineyard" x1="0" y1="0" x2="1" y2="1">
        <stop offset="0" stop-color="#3f6a2c"/>
        <stop offset="0.5" stop-color="#7da34a"/>
        <stop offset="1" stop-color="#4f7a33"/>
      </linearGradient>
      <linearGradient id="basketSky" x1="0" y1="0" x2="0" y2="1">
        <stop offset="0" stop-color="#c9d7e6"/>
        <stop offset="0.5" stop-color="#8a6a4c"/>
        <stop offset="1" stop-color="#dfe6ec"/>
      </linearGradient>
      <linearGradient id="skyVines" x1="0" y1="0" x2="0" y2="1">
        <stop offset="0" stop-color="#4f7ac8"/>
        <stop offset="0.6" stop-color="#a9bfe0"/>
        <stop offset="1" stop-color="#4e6b2c"/>
      </linearGradient>
      <linearGradient id="sunrise" x1="0" y1="0" x2="0" y2="1">
        <stop offset="0" stop-color="#8a96a8"/>
        <stop offset="0.35" stop-color="#f1d27a"/>
        <stop offset="0.55" stop-color="#6c7a70"/>
        <stop offset="1" stop-color="#3f6a33"/>
      </linearGradient>
    </defs>

    <!-- panels -->
    <rect x="0" y="0" width="400" height="849" fill="var(--white)"/>
    <rect x="400" y="0" width="400" height="849" fill="url(#darkPanel)"/>
    <rect x="800" y="0" width="400" height="849" fill="var(--blue-panel)"/>
    <path d="M800 0 H1200 V232 H815 Q800 232 800 247 Z" fill="var(--blue-bright)"/>

    <!-- lower-right white sweep -->
    <path d="M600 849 Q820 640 1060 650 Q1140 640 1200 648 V849 Z" fill="var(--white)"/>
    <path d="M610 849 Q760 720 840 690" fill="none" stroke="var(--blue-bright)" stroke-width="1.5"/>
    <path d="M1170 641 Q1190 642 1200 645" fill="none" stroke="var(--blue-bright)" stroke-width="3"/>

    <!-- top swoosh band and aerial area -->
    <path d="M0 280 Q200 330 420 270 Q560 220 650 110 L690 0 H700 L690 0 Q640 200 420 300 Q220 380 0 360 Z" fill="var(--blue-bright)"/>
    <path d="M0 360 Q250 380 420 300 L400 310 V395 Q200 380 0 385 Z" fill="var(--white)"/>
    <path d="M0 0 H675 Q620 210 400 290 Q200 330 0 280 Z" fill="url(#vineyard)" role="img" aria-label="Aerial photo of a hot air balloon drifting over green vineyards"/>
    <path d="M665 0 L690 0 Q660 180 420 295 L400 300 Q600 200 665 0 Z" fill="var(--blue-bright)"/>
    <path d="M356 330 Q450 300 520 230" fill="none" stroke="var(--blue-bright)" stroke-width="1.5"/>
    <path d="M0 385 Q30 388 50 388" fill="none" stroke="var(--blue-bright)" stroke-width="1.5"/>

    <!-- left circle photo -->
    <circle cx="205" cy="365" r="155" fill="var(--white)"/>
    <circle cx="205" cy="365" r="141" fill="url(#basketSky)" role="img" aria-label="Photo of passengers waving from a balloon basket"/>

    <!-- middle top circle photo -->
    <circle cx="619" cy="172" r="118" fill="var(--ink-dark)"/>
    <circle cx="619" cy="172" r="107" fill="url(#skyVines)" role="img" aria-label="Photo of a balloon in blue sky above grapevine leaves"/>

    <!-- right circle photo -->
    <circle cx="1000" cy="650" r="170" fill="var(--white)"/>
    <circle cx="1000" cy="650" r="154" fill="url(#sunrise)" role="img" aria-label="Photo of balloons over the valley at sunrise"/>
  </svg>

  <section class="text cover">
    <h1 class="cover-headline script">Experience</h1>
    <p class="cover-sub">the beautiful<br>Hunter Valley in a hot air balloon</p>
    <p class="cover-phone">1300 UP HIGH</p>
    <p class="cover-digits">(1300 874 444)</p>
    <p class="cover-web">www.skywardballooning.com.au</p>
  </section>

  <article class="text feature-mid" style="top:322px">
    <h2 class="feature-title script">Experienced Pilots &amp; Crew</h2>
    <p class="feature-body">Skyward Ballooning pilots and crew are highly trained professionals which operate under the strict control of the Civil Aviation Safety Authority. Skyward Ballooning deliver Australia's best hot air ballooning experience in a fun yet safe environment.</p>
  </article>

  <article class="text feature-mid" style="top:490px">
    <h2 class="feature-title script">Award Winning Service</h2>
    <p class="feature-body">Skyward Ballooning is an accredited tourism business and has been the winner of numerous NSW &amp; Regional Tourism awards. Skyward Ballooning strives to be the leader in the ballooning industry through all aspects of our business.</p>
  </article>

  <article class="text feature-mid" style="top:655px">
    <h2 class="feature-title script">High Flexibility</h2>
    <p class="feature-body">Skyward Ballooning offers a 100% flight fee refund if your flight is cancelled due to weather.</p>
  </article>

  <div class="text brand-name"><span class="brand-dot"></span>Skyward Ballooning</div>

  <article class="text feature-right panel-right" style="top:36px">
    <h2 class="feature-title script">Daily Flights</h2>
    <p class="feature-body">Flights take place daily at sunrise in the Hunter Valley. Enjoy one hour of breathtaking views of Australia's oldest wine growing region and surrounds. A champagne breakfast concludes the morning at a local restaurant.</p>
  </article>

  <article class="text feature-right panel-right" style="top:272px">
    <h2 class="feature-title script">Digital Photo Package</h2>
    <p class="feature-body">Skyward Ballooning provides access to digital photography from all flights to capture those special moments for you to share with friends and family.</p>
  </article>
</div>
</body>
</html>
```